CD-Cover Desig für neues Album eines Liedermacher-Duos
Zielgruppe
Wir sind ein Liedermacher-Duo und benötigen für unser neues Album mit dem Titel 'Kiesel' ein Cover.
Infos über den Themenbereich der Songs findet man hier: https://www.vorhabenwerk.de/cd-kiesel
Aufgabenstellung
Cover könnte schlicht sein... oder auch kreativ verspielt mit warmen Farben und Formen... aber nicht kitschig.
'Kiesel' im Sinne von Geborgenheit also kein verzehrendes Feuer.. eher sonnig.
Evtl. könnte man unsere beiden Hauptinstrumente (Geige und Gitarre) andeuten.
Sonst stehen auf dem Cover nur noch unsere Namen: Dorothea Lindner & Jörg Haberl

```html
<!DOCTYPE html>
<html lang="de">
<head>
<meta charset="utf-8">
<title>Kiesel – Dorothea Lindner &amp; Jörg Haberl</title>
<link rel="stylesheet" href="https://fonts.googleapis.com/css2?family=Barlow:wght@400&family=Damion&display=swap">
<style>
  :root {
    --tone-top: #d06f35;
    --tone-mid: #ec9147;
    --tone-warm: #f0a050;
    --tone-low: #b4683c;
    --frame-line: #ffe6a8;
    --name-white: #ffffff;
    --title-tint: rgba(255, 226, 170, 0.6);
  }
  * { margin: 0; padding: 0; box-sizing: border-box; }
  html, body {
    width: 1200px;
    height: 1200px;
    overflow: hidden;
    background: var(--tone-top);
  }
  .cover {
    position: relative;
    width: 1200px;
    height: 1200px;
    overflow: hidden;
  }
  .cover-photo {
    position: absolute;
    inset: 0;
    background: linear-gradient(180deg, var(--tone-top) 0%, var(--tone-mid) 40%, var(--tone-warm) 60%, var(--tone-mid) 80%, var(--tone-low) 100%);
  }
  .cover-frame {
    position: absolute;
    left: 20px;
    top: 20px;
    width: 1160px;
    height: 1160px;
    border: 3px solid var(--frame-line);
  }
  .artist-box {
    position: absolute;
    left: 63px;
    top: 63px;
    width: 386px;
    height: 119px;
    border: 2px solid var(--name-white);
    display: flex;
    align-items: center;
    justify-content: center;
  }
  .artist-names {
    font-family: "Barlow", sans-serif;
    font-weight: 400;
    font-size: 35px;
    line-height: 46px;
    color: var(--name-white);
    text-align: center;
  }
  .album-title {
    position: absolute;
    left: 0;
    top: 0;
    width: 1200px;
    height: 1200px;
  }
  .album-title text {
    font-family: "Damion", cursive;
    font-size: 470px;
    fill: var(--title-tint);
  }
</style>
</head>
<body>
  <main class="cover">
    <div class="cover-photo" role="img" aria-label="Foto: Gräser als Silhouetten vor tief stehender Sonne im orangefarbenen Abendhimmel"></div>
    <div class="cover-frame"></div>
    <div class="artist-box">
      <p class="artist-names">Dorothea Lindner &amp;<br>Jörg Haberl</p>
    </div>
    <svg class="album-title" viewBox="0 0 1200 1200" aria-labelledby="album-title-text">
      <text id="album-title-text" x="10" y="995" textLength="1100" lengthAdjust="spacingAndGlyphs">Kiesel</text>
    </svg>
  </main>
</body>
</html>
```